House Builder and Property Development Card Design and Logo

I need a business card design for a building and property development company.
Colour scheme of Dark Grey and Green, I would like it bold, sharp and professional.
No logo yet done, I'm open to options but please stay away from the usual- house, roof, hammers etc.
Thanks Rob

Please be aware that on the business card information section the WHRC # 5528391 is a licence number and my phone number 0492837165. The numbers are close together and could be mistaken as one whole number 

Thank you

                                   

Industry/Entity Type

Building

Contact Information for Business Card

VARGA BUILD & DEVELOPMENT.
Residential Building & Property Development
Robert Varga - Director
WHRC # 5528391
0492837165
rob@vargabuild.example.com.au

Requirements
Must have
• Bold Business name
Dark grey and green colours
Should not have
• roof outline or hammer logo

```html
<!DOCTYPE html>
<html lang="en">
<head>
<meta charset="utf-8">
<title>Varga Build &amp; Development — Business Card</title>
<link href="https://fonts.googleapis.com/css2?family=Open+Sans:wght@400;600;700;800&display=swap" rel="stylesheet">
<style>
  :root {
    --bg: #2a2b2d;
    --card-dark: #272b30;
    --card-dark-edge: #1f2226;
    --green: #7dbb3a;
    --green-light: #8cc640;
    --white: #ffffff;
    --paper: #f3f3f3;
    --grey-text: #c9ccd0;
    --grey-mid: #6b6f74;
    --grey-faint: #3d4248;
    --ink: #1e2124;
  }
  * { box-sizing: border-box; margin: 0; padding: 0; }
  html, body {
    width: 1200px; height: 1000px; overflow: hidden;
    background: var(--bg);
    font-family: "Open Sans", Arial, sans-serif;
  }
  .canvas {
    position: relative; width: 1200px; height: 1000px;
    display: flex; flex-direction: column; align-items: center; justify-content: center; gap: 36px;
  }
  .card {
    position: relative; width: 780px; height: 446px; overflow: hidden;
    background: var(--card-dark);
    box-shadow: 0 10px 30px rgba(0,0,0,.45);
  }

  /* Back side */
  .card-back .band {
    position: absolute; left: 0; right: 0; top: 92px; height: 166px;
    background: var(--green-light);
    display: flex; align-items: center; justify-content: center;
  }
  .wordmark { display: flex; align-items: center; gap: 16px; }
  .wordmark .mark-square { width: 54px; height: 54px; }
  .wordmark .divider { width: 2px; height: 58px; }
  .wordmark .text { display: flex; flex-direction: column; line-height: 1; }
  .wordmark .name { font-weight: 800; font-size: 52px; letter-spacing: .5px; }
  .wordmark .tagline { font-weight: 600; font-size: 13px; letter-spacing: 3.2px; margin-top: 4px; }

  .card-back .mark-square { background: var(--white); }
  .card-back .divider { background: rgba(255,255,255,.7); }
  .card-back .name, .card-back .tagline { color: var(--white); }

  /* Front side */
  .card-front .top {
    position: absolute; left: 0; right: 0; top: 0; height: 178px;
    background: linear-gradient(180deg, var(--white), var(--paper));
    padding: 64px 0 0 44px;
  }
  .card-front .mark-square { background: var(--ink); }
  .card-front .divider { background: var(--grey-mid); }
  .card-front .name { color: var(--green); }
  .card-front .tagline { color: var(--grey-mid); }
  .card-front .rule {
    position: absolute; left: 0; right: 0; top: 178px; height: 3px; background: var(--green);
  }
  .card-front .dash-strip {
    position: absolute; left: 0; right: 0; top: 181px; height: 6px;
    background: repeating-linear-gradient(90deg, #5b6066 0 8px, transparent 8px 14px);
    opacity: .7;
  }
  .person { position: absolute; left: 44px; top: 216px; }
  .person .full-name { color: var(--green); font-weight: 700; font-size: 30px; line-height: 1.1; }
  .person .role { color: var(--white); font-weight: 600; font-size: 16px; margin-top: 2px; }
  .contact {
    position: absolute; right: 40px; top: 208px;
    list-style: none; font-size: 17px; line-height: 1.55; color: var(--grey-text);
  }
  .contact .label { color: var(--green); font-weight: 600; }
  .licence {
    position: absolute; left: 44px; bottom: 30px;
    color: var(--grey-faint); font-size: 15px; font-weight: 600; letter-spacing: .5px;
  }
</style>
</head>
<body>
<main class="canvas">
  <section class="card card-back" aria-label="Business card back">
    <div class="band">
      <div class="wordmark">
        <span class="mark-square"></span>
        <span class="divider"></span>
        <div class="text">
          <span class="name">Varga</span>
          <span class="tagline">BUILD &amp; DEVELOPMENT</span>
        </div>
      </div>
    </div>
  </section>

  <section class="card card-front" aria-label="Business card front">
    <header class="top">
      <div class="wordmark">
        <span class="mark-square"></span>
        <span class="divider"></span>
        <div class="text">
          <span class="name">Varga</span>
          <span class="tagline">BUILD &amp; DEVELOPMENT</span>
        </div>
      </div>
    </header>
    <div class="rule"></div>
    <div class="dash-strip"></div>

    <div class="person">
      <p class="full-name">Robert Varga</p>
      <p class="role">Director</p>
    </div>

    <ul class="contact">
      <li><span class="label">Phone</span> : 0492 837165</li>
      <li><span class="label">Email</span> : rob@vargabuild.example.com.au</li>
      <li><span class="label">Website</span> : www.vargabuild.example.com.au</li>
    </ul>

    <p class="licence">WHRC # 5528391</p>
  </section>
</main>
</body>
</html>
```